Brocure for Brindlo - Social Media Management

Brindlo is a Dutch company in the market of Social Media growth. We need a brochure (digital/PDF) for our company. Please see attached word doc for the text and attached logo. The initial proposal can contain just the first 4 pages text of the word doc.

We use informal language in all our communication.

Slogan: Effectieve Social Media Marketing voor professionals en ondernemers

Website: brindlopq.nl

Industry/Entity Type

Digital Marketing

Contact Information for Business Card

Contact details:

Joris ter Haaksel
joris@brindlopq.nl
06-47915328

```html
<!DOCTYPE html>
<html lang="nl">
<head>
<meta charset="utf-8">
<title>Brindlo – Social Media Management brochure</title>
<link href="https://fonts.googleapis.com/css2?family=Poppins:wght@400;800&display=swap" rel="stylesheet">
<style>
  :root {
    --page-bg: #ededed;
    --navy: #0b2242;
    --orange: #f07236;
    --orange-deep: #ef5a24;
    --orange-light: #f79257;
    --body-text: #4f4f4f;
  }
  html, body {
    margin: 0;
    padding: 0;
    width: 1200px;
    height: 1200px;
    overflow: hidden;
    background: var(--page-bg);
  }
  .brochure-page {
    position: relative;
    width: 1200px;
    height: 1200px;
    overflow: hidden;
    background: var(--page-bg);
    font-family: "Poppins", sans-serif;
  }
  .backdrop-photo {
    position: absolute;
    inset: 0;
    background:
      radial-gradient(ellipse at 62% 55%, rgba(180,180,180,0.45), rgba(237,237,237,0) 60%),
      radial-gradient(ellipse at 85% 30%, rgba(200,200,200,0.35), rgba(237,237,237,0) 45%),
      linear-gradient(180deg, #f0f0f0 0%, #e6e6e6 60%, #dedede 100%);
  }
  .corner-shapes {
    position: absolute;
    top: 0;
    left: 0;
  }
  .section {
    position: absolute;
    margin: 0;
  }
  .section-title {
    margin: 0;
    color: var(--orange);
    font-weight: 800;
    font-size: 30px;
    line-height: 37px;
    letter-spacing: -0.1px;
  }
  .section-text {
    margin: 0;
    color: var(--body-text);
    font-weight: 400;
    font-size: 18.2px;
    line-height: 23.3px;
    hyphens: auto;
  }
  .col-left { left: 78px; width: 485px; }
  .col-right { left: 641px; width: 482px; }
</style>
</head>
<body>
<div class="brochure-page">
  <div class="backdrop-photo" role="img" aria-label="Faded background photo of cubes with social media icons"></div>

  <svg class="corner-shapes" width="1200" height="220" viewBox="0 0 1200 220" aria-hidden="true">
    <defs>
      <linearGradient id="orangeLeft" x1="0" y1="0" x2="1" y2="1">
        <stop offset="0" stop-color="#ef5a24"/>
        <stop offset="1" stop-color="#f79257"/>
      </linearGradient>
      <linearGradient id="orangeRight" x1="0" y1="0" x2="1" y2="0">
        <stop offset="0" stop-color="#f79257"/>
        <stop offset="1" stop-color="#ef5a24"/>
      </linearGradient>
    </defs>
    <polygon points="60,0 1200,0 1031,9 99,78" fill="var(--navy)"/>
    <polygon points="0,0 236,0 56,102 0,214" fill="url(#orangeLeft)"/>
    <polygon points="0,0 105,0 56,102 0,214" fill="var(--orange-deep)" opacity="0.55"/>
    <polygon points="1031,9 1200,0 1200,75 1155,75" fill="url(#orangeRight)"/>
    <polygon points="1155,75 1200,75 1200,211" fill="var(--orange-light)"/>
  </svg>

  <section class="section col-left" style="top:148px">
    <h2 class="section-title">Waarom kies je voor ons?</h2>
  </section>
  <p class="section section-text col-left" style="top:209px">Jij hebt jouw vak, wij het onze. Als iedereen doet waar hij goed in is, worden daar allemaal beter van. Wij zijn goed in het activeren en vergroten van je sociale netwerk. Daarvoor gebruiken we een slimme mix van kennis en tools.</p>
  <p class="section section-text col-left" style="top:349px">Een strategie die ervoor zorgt dat jij je kunt focussen op je corebusiness. Met onze slimme tools vergroten wij de impact van je sociale netwerken. Met als resultaat: meer traffic, meer leads, meer omzet.</p>

  <section class="section col-left" style="top:484px">
    <h2 class="section-title">Doen we alles zelf?</h2>
  </section>
  <p class="section section-text col-left" style="top:548px">Wij zijn slim in de strategie en systemen voor het vergroten van interactie. En we hebben een netwerk van specialisten die slim zijn in hun vak. Zoals een reclamebureau, creatief ontwerper, websitebouwer of marketingstrategiebureau.</p>
  <p class="section section-text col-left" style="top:688px">Is er op dat vlak een behoefte, dan brengen wij je graag in contact.</p>

  <section class="section col-left" style="top:779px">
    <h2 class="section-title">Hoe lang gaan we met elkaar in zee?</h2>
  </section>
  <p class="section section-text col-left" style="top:880px">Een groeistrategie werkt op de lange termijn het beste als die groei organisch is. En dat vraagt dus ook een strategie voor de lange termijn. Lang is relatief, maar je moet erop rekenen dat we minimaal een jaar nodig hebben om de groeistrategie optimaal te laten werken.</p>
  <p class="section section-text col-left" style="top:1020px">Natuurlijk is er in elke situatie snelle winst te behalen. Maar voor een goede samenwerking is het belangrijk dat je elkaar leert kennen en begrijpen. Daarom vragen we ook regelmatig jouw energie en input.</p>

  <section class="section col-right" style="top:148px">
    <h2 class="section-title">Groeien op sociale media</h2>
  </section>
  <p class="section section-text col-right" style="top:210px">Het staat als een paal boven water: sociale media zijn een krachtig marketinginstrument. Een kans die je niet voorbij kunt laten gaan, of je dat nou leuk vindt of niet. Het geeft je de kans om je merk op te bouwen, je zicht- en vindbaarheid te verbeteren en uiteindelijk meer leads en verkopen te genereren.</p>
  <p class="section section-text col-right" style="top:374px">Het beheren van je sociale platforms is een tijdrovende klus. En om resultaat te krijgen, moet je het ook nog eens slim doen. Om de online herkenbaarheid van je bedrijf te vergroten, zijn je uitingen de sleutel.</p>
  <p class="section section-text col-right" style="top:491px">Interactie, consistentie, responsiveness, allemaal zorgen ze voor herkenning en betrokkenheid van je volgers. We helpen je om je digitale activiteiten met elkaar te verbinden en je bedrijf te laten groeien.</p>

  <section class="section col-right" style="top:621px">
    <h2 class="section-title">Volledig sociaal management</h2>
  </section>
  <p class="section section-text col-right" style="top:684px">We bieden een compleet beheerpakket voor sociale media waarmee we betrokkenheid van volgers realiseren en tijdig en altijd proactief schakelen naar de volgende stap. Zo blijven bezoekers geboeid en actief.</p>
  <p class="section section-text col-right" style="top:801px">We plannen zowel doelgroep- als branche specifieke inhoud en combineren online aanwezigheid om meer en meer gericht websiteverkeer te genereren.</p>

  <section class="section col-right" style="top:914px">
    <h2 class="section-title">Activeren van je netwerk</h2>
  </section>
  <p class="section section-text col-right" style="top:985px">Je bent al een poos bezig met het beheren van je sociale media, maar ziet geen commercieel resultaat? De specialist maakt het verschil. Jouw kennis van jouw product en klant, gecombineerd met ons specialisme over sociale media. In zeer diverse branches.</p>
</div>
</body>
</html>
```